Brochure Design Project

PLEASE USE THE ATTACHED WORD DOC ONLY AS A GUIDE- I WANT TO SEE A TRUE DESIGN AND NOT JUST A RECREATE OF MY CONTENT.

We need a brochure that is geared towards a service mentality. less tech/bold and something very approachable.

we will look for a design concept and then finalize the content laters.

Target Market(s)

nurses and business owners

Industry/Entity Type

Tech

```html
<!DOCTYPE html>
<html lang="en">
<head>
<meta charset="utf-8">
<title>Harborview Pharmacy Services – Tri-fold Brochure</title>
<link rel="stylesheet" href="https://fonts.googleapis.com/css2?family=Montserrat:wght@800&family=Questrial&display=swap">
<style>
  :root {
    --bg: #d9dadc;
    --blue-top: #1d9ad8;
    --blue-bottom: #2c5ea8;
    --white: #ffffff;
    --silver-light: #f1f1f2;
    --silver-dark: #b9bbbe;
    --ink: #2b2b2d;
    --tile-blue: #3a8fc4;
  }
  * { margin: 0; padding: 0; box-sizing: border-box; }
  html, body { width: 1200px; height: 1000px; overflow: hidden; }
  body {
    background: var(--bg);
    font-family: "Questrial", sans-serif;
    position: relative;
  }

  .panel {
    position: absolute;
    top: 60px;
    width: 410px;
    height: 880px;
    overflow: hidden;
    box-shadow: 0 6px 18px rgba(0,0,0,0.18);
  }

  /* Back panel */
  .panel--back {
    left: 160px;
    background: linear-gradient(180deg, var(--blue-top) 0%, var(--blue-top) 55%, var(--blue-bottom) 100%);
    color: var(--white);
  }
  .back-pattern {
    position: absolute;
    left: 60px; top: -120px;
    width: 440px; height: 720px;
    background: radial-gradient(closest-side, rgba(255,255,255,0.8) 0%, rgba(255,255,255,0.4) 45%, rgba(255,255,255,0) 100%);
  }
  .back-frame {
    position: absolute;
    left: 0; top: 0;
    width: 410px; height: 400px;
  }
  .back-brand {
    position: absolute;
    left: 0; right: 0;
    top: 590px;
    text-align: center;
  }
  .back-brand .brand-mark {
    display: block;
    width: 16px; height: 16px;
    margin: 0 auto 10px;
    background: var(--white);
  }
  .back-brand .brand-name {
    font-size: 40px;
    line-height: 1;
    letter-spacing: -0.5px;
  }
  .back-brand .brand-sub {
    font-size: 11px;
    letter-spacing: 3px;
    margin-top: 6px;
  }
  .back-contact {
    position: absolute;
    left: 0; right: 0;
    top: 700px;
    text-align: center;
    font-size: 13px;
    line-height: 1.5;
    font-style: normal;
  }

  /* Front panel */
  .panel--front {
    left: 630px;
    background: linear-gradient(160deg, var(--silver-dark) 0%, var(--silver-light) 45%, #ffffff 60%, var(--silver-dark) 100%);
    color: var(--ink);
  }
  .front-pattern {
    position: absolute;
    left: -40px; top: 0;
    width: 480px; height: 560px;
    background: radial-gradient(closest-side, rgba(120,150,175,0.38) 0%, rgba(120,150,175,0.2) 50%, rgba(120,150,175,0) 100%);
  }
  .headline {
    position: absolute;
    left: 40px; top: 70px;
    width: 340px;
  }
  .headline-big {
    display: flex;
    align-items: flex-end;
    white-space: nowrap;
  }
  .headline-big .big {
    font-family: "Montserrat", sans-serif;
    font-weight: 800;
    font-size: 68px;
    line-height: 0.9;
    letter-spacing: -1px;
  }
  .headline-big .stack {
    display: flex;
    flex-direction: column;
    align-items: flex-start;
    margin-left: 10px;
  }
  .headline-big .city {
    font-family: "Montserrat", sans-serif;
    font-weight: 800;
    font-size: 46px;
    line-height: 0.95;
    letter-spacing: -1px;
  }
  .headline-big .support {
    font-size: 22px;
    border: 2px solid var(--ink);
    padding: 0 8px;
    margin-top: 2px;
    line-height: 1.2;
  }
  .headline-small {
    margin-top: 44px;
    white-space: nowrap;
  }
  .headline-small .small-town {
    display: inline-block;
    font-size: 40px;
    border: 2px solid var(--ink);
    padding: 2px 12px;
    line-height: 1.1;
  }
  .headline-small .service {
    display: block;
    font-size: 28px;
    margin-left: 150px;
    margin-top: 4px;
  }

  .front-brand {
    position: absolute;
    left: 0; right: 0;
    top: 560px;
    text-align: center;
  }
  .front-brand .brand-mark {
    display: block;
    width: 26px; height: 26px;
    margin: 0 auto 20px;
    background: var(--tile-blue);
  }
  .front-brand .brand-name {
    font-size: 64px;
    line-height: 1;
    letter-spacing: -1px;
  }
  .front-brand .brand-sub {
    font-size: 15px;
    letter-spacing: 4px;
    margin-top: 10px;
  }
</style>
</head>
<body>

  <section class="panel panel--back" aria-label="Brochure back cover">
    <div class="back-pattern" role="img" aria-label="Large white tile decoration"></div>
    <svg class="back-frame" viewBox="0 0 410 400" aria-hidden="true">
      <polyline points="70,160 230,160 230,400" fill="none" stroke="#ffffff" stroke-width="2"/>
    </svg>
    <div class="back-brand">
      <span class="brand-mark" aria-hidden="true"></span>
      <div class="brand-name">harborview</div>
      <div class="brand-sub">PHARMACY SERVICES</div>
    </div>
    <address class="back-contact">
      450 Marlow Ave Suite 210<br>
      Phone: (555) 014-2290<br>
      After Hours/On Call: (555) 014-2291
    </address>
  </section>

  <section class="panel panel--front" aria-label="Brochure front cover">
    <div class="front-pattern" role="img" aria-label="Faint blue tile decoration"></div>
    <div class="headline">
      <div class="headline-big">
        <span class="big">Big</span>
        <span class="stack">
          <span class="city">City</span>
          <span class="support">Support.</span>
        </span>
      </div>
      <div class="headline-small">
        <span class="small-town">Small Town</span>
        <span class="service">Service.</span>
      </div>
    </div>
    <div class="front-brand">
      <span class="brand-mark" aria-hidden="true"></span>
      <div class="brand-name">harborview</div>
      <div class="brand-sub">PHARMACY SERVICES, INC</div>
    </div>
  </section>

</body>
</html>
```